Mesh Banner Design for Business Premises

We require the design of a large mesh banner to be installed across the front fence of our warehouse. The banner should prominently feature our existing Trelborn logo and brand colours (yellow, white, and black) and be designed to be highly visible from the road.

The overall aesthetic should be strong, masculine, and industrial, reflecting the nature of the scaffolding and construction industry. The background should be predominantly black, with our branding incorporated in yellow and white for strong contrast and readability.

The banner should clearly communicate the full scope of services we provide, including:

Scaffold Design
Scaffold Engineering
Scaffold Installation / Erection
Scaffold Dismantling

It should also indicate the types of projects and clients we service, including:

Commercial
Industrial
Residential
Civil

The design should feel bold and professional, with a construction-oriented style that aligns with the scaffolding industry. It should be clean, impactful, and easy to read from a distance, ensuring passing traffic can quickly understand our services.

Where possible, subtle industrial or structural design elements (such as scaffold components, steel textures, or linework) may be incorporated into the background to reinforce the industry theme while keeping the layout uncluttered.

The final design will be produced as a large-format mesh banner for outdoor installation, so it should be created with this application and viewing distance in mind.

```html
<!DOCTYPE html>
<html lang="en">
<head>
<meta charset="utf-8">
<title>Trelborn – Mesh Fence Banner</title>
<link href="https://fonts.googleapis.com/css2?family=Barlow:wght@600;700&display=swap" rel="stylesheet">
<style>
  :root {
    --page-bg: #f4f4f4;
    --banner-black: #0d0d0d;
    --banner-grey: #1c1c1c;
    --brand-yellow: #f2ab1b;
    --brand-white: #f3f3f3;
    --rule-yellow: rgba(242, 171, 27, 0.7);
  }
  * { margin: 0; padding: 0; box-sizing: border-box; }
  html, body {
    width: 1200px;
    height: 800px;
    overflow: hidden;
    background: var(--page-bg);
  }
  body { position: relative; font-family: "Barlow", Arial, sans-serif; }

  .banner {
    position: absolute;
    left: 0;
    top: 132px;
    width: 1200px;
    height: 536px;
    background: var(--banner-black);
    overflow: hidden;
  }
  .structure-backdrop {
    position: absolute;
    inset: 0;
    background:
      radial-gradient(ellipse 520px 300px at 300px 430px, rgba(70, 60, 40, 0.35), transparent 70%),
      radial-gradient(ellipse 420px 320px at 1050px 180px, rgba(60, 60, 60, 0.35), transparent 70%),
      linear-gradient(135deg, var(--banner-grey) 0%, var(--banner-black) 55%, #141414 100%);
  }

  .brand {
    position: absolute;
    left: 42px;
    top: 0;
    width: 400px;
    height: 536px;
    display: flex;
    flex-direction: column;
    align-items: center;
    justify-content: center;
    gap: 34px;
  }
  .brand-square {
    width: 120px;
    height: 120px;
    background: var(--brand-yellow);
  }
  .brand-name {
    font-weight: 700;
    font-size: 62px;
    letter-spacing: 5px;
    color: var(--brand-white);
    text-transform: uppercase;
    line-height: 1;
  }

  .services {
    position: absolute;
    left: 477px;
    top: 70px;
    list-style: none;
  }
  .services li {
    display: flex;
    align-items: center;
    height: 67px;
    font-weight: 600;
    font-size: 37px;
    color: var(--brand-white);
  }
  .chevron {
    width: 22px;
    height: 26px;
    margin-right: 13px;
    flex: none;
  }

  .sectors {
    position: absolute;
    left: 478px;
    top: 350px;
    width: 722px;
    height: 135px;
    border-top: 1.5px solid var(--rule-yellow);
    border-left: 1.5px solid var(--rule-yellow);
  }
  .sectors::before {
    content: "";
    position: absolute;
    left: 0;
    right: 0;
    top: 68px;
    border-top: 1.5px solid var(--rule-yellow);
  }
  .sectors::after {
    content: "";
    position: absolute;
    left: 346px;
    top: 69px;
    bottom: 0;
    border-left: 1.5px solid var(--rule-yellow);
  }
  .sector {
    position: absolute;
    font-weight: 700;
    font-size: 39px;
    color: var(--brand-yellow);
    text-transform: uppercase;
    line-height: 1;
    letter-spacing: 0.5px;
  }
  .sector--commercial { left: 29px; top: 16px; }
  .sector--industrial { left: 380px; top: 16px; }
  .sector--residential { left: 29px; top: 84px; }
  .sector--civil { left: 380px; top: 84px; }

  .hazard-stripes {
    position: absolute;
    left: 0;
    bottom: 0;
    width: 290px;
    height: 54px;
    background: repeating-linear-gradient(
      55deg,
      var(--brand-yellow) 0 22px,
      transparent 22px 48px
    );
    -webkit-mask-image: linear-gradient(90deg, #000 30%, transparent 100%);
    mask-image: linear-gradient(90deg, #000 30%, transparent 100%);
  }
</style>
</head>
<body>
  <main class="banner">
    <div class="structure-backdrop" role="img" aria-label="Faint scaffold structure linework across a dark steel background"></div>

    <div class="brand">
      <div class="brand-square"></div>
      <div class="brand-name">Trelborn</div>
    </div>

    <ul class="services">
      <li><svg class="chevron" viewBox="0 0 22 26"><polygon points="0,0 9,0 22,13 9,26 0,26 13,13" fill="#f2ab1b"/></svg>Scaffold Design</li>
      <li><svg class="chevron" viewBox="0 0 22 26"><polygon points="0,0 9,0 22,13 9,26 0,26 13,13" fill="#f2ab1b"/></svg>Scaffold Engineering</li>
      <li><svg class="chevron" viewBox="0 0 22 26"><polygon points="0,0 9,0 22,13 9,26 0,26 13,13" fill="#f2ab1b"/></svg>Scaffold Installation / Erection</li>
      <li><svg class="chevron" viewBox="0 0 22 26"><polygon points="0,0 9,0 22,13 9,26 0,26 13,13" fill="#f2ab1b"/></svg>Scaffold Dismantling</li>
    </ul>

    <div class="sectors">
      <span class="sector sector--commercial">Commercial</span>
      <span class="sector sector--industrial">Industrial</span>
      <span class="sector sector--residential">Residential</span>
      <span class="sector sector--civil">Civil</span>
    </div>

    <div class="hazard-stripes"></div>
  </main>
</body>
</html>
```